Business Card Design

I used to run a Mountaineering school and am getting back into business and just want a generic type card with an adventure theme. Core activities will be mountaineering, rock climbing, canyoning, expeditions, cross country skiing,

Industry/Entity Type

School

Contact Information for Business Card

Colin Ashby Adventure Guide
email: tallpinecolin@mailvane.net
+61472 836 915.

```html
<!DOCTYPE html>
<html lang="en">
<head>
<meta charset="utf-8">
<title>Colin Ashby – Adventure Guide</title>
<link rel="stylesheet" href="https://fonts.googleapis.com/css2?family=Exo+2:wght@500;600;700&display=swap">
<style>
  :root {
    --sky-blue: #0f7ff0;
    --trail-orange: #f5a02f;
    --paper: #ffffff;
    --mist: rgba(255, 255, 255, 0.55);
  }
  * { margin: 0; padding: 0; box-sizing: border-box; }
  html, body {
    width: 1200px;
    height: 741px;
    overflow: hidden;
    background: var(--paper);
  }
  .card {
    position: relative;
    width: 1200px;
    height: 741px;
    background: var(--paper);
    font-family: "Exo 2", sans-serif;
  }
  .brand {
    position: absolute;
    left: 100px;
    top: 124px;
    display: flex;
    align-items: center;
    gap: 16px;
  }
  .brand-dot {
    width: 26px;
    height: 26px;
    border-radius: 50%;
    background: var(--sky-blue);
  }
  .brand-name {
    font-size: 46px;
    font-weight: 600;
    color: var(--trail-orange);
    letter-spacing: 0.5px;
  }
  .activities {
    position: absolute;
    right: 76px;
    top: 158px;
    list-style: none;
    text-align: right;
  }
  .activity {
    font-size: 22px;
    font-weight: 600;
    color: var(--sky-blue);
    line-height: 26px;
    height: 33px;
    border-bottom: 3px solid var(--trail-orange);
    padding-left: 4px;
    margin-left: auto;
    width: max-content;
    min-width: 100%;
  }
  .activity:nth-child(1) { width: 200px; }
  .activity:nth-child(2) { width: 230px; }
  .activity:nth-child(3) { width: 255px; }
  .activity:nth-child(4) { width: 302px; }
  .activity:nth-child(5) { width: 345px; height: 40px; padding-top: 7px; }
  .activity { text-align: left; }
  .band {
    position: absolute;
    left: 76px;
    top: 430px;
    width: 1048px;
    height: 232px;
    background: var(--sky-blue);
  }
  .base-stripe {
    position: absolute;
    left: 76px;
    top: 662px;
    width: 1048px;
    height: 28px;
  }
  .guide-name {
    position: absolute;
    left: 126px;
    top: 364px;
    font-size: 50px;
    font-weight: 600;
    color: var(--sky-blue);
  }
  .contact {
    position: absolute;
    left: 124px;
    display: flex;
    align-items: center;
    gap: 24px;
    font-size: 26px;
    font-weight: 600;
    color: var(--trail-orange);
  }
  .contact-email { top: 466px; }
  .contact-phone { top: 530px; }
  .contact-icon { flex: none; }
  .peak-artwork {
    position: absolute;
    left: 700px;
    top: 368px;
    width: 400px;
    height: 194px;
    border-radius: 6px;
    background: linear-gradient(160deg, #e4f0fc 0%, var(--mist) 60%, rgba(255,255,255,0.25) 100%);
  }
  .role {
    position: absolute;
    right: 102px;
    top: 614px;
    font-size: 31px;
    font-weight: 600;
    color: var(--trail-orange);
  }
</style>
</head>
<body>
  <div class="card">
    <div class="brand">
      <span class="brand-dot"></span>
      <span class="brand-name">Brenna Ridge</span>
    </div>

    <ul class="activities">
      <li class="activity">Mountaineering</li>
      <li class="activity">Rock climbing</li>
      <li class="activity">Canyoning</li>
      <li class="activity">Expeditions</li>
      <li class="activity">Cross Country Skiing</li>
    </ul>

    <h1 class="guide-name">Colin Ashby</h1>

    <div class="band"></div>
    <svg class="base-stripe" viewBox="0 0 1048 28" aria-hidden="true">
      <polygon points="0,0 668,0 640,28 0,28" fill="var(--trail-orange)"/>
      <polygon points="668,0 688,0 660,28 640,28" fill="var(--sky-blue)"/>
      <polygon points="688,0 1048,0 1048,28 660,28" fill="var(--trail-orange)"/>
    </svg>

    <div class="contact contact-email">
      <svg class="contact-icon" width="60" height="40" viewBox="0 0 60 40" aria-hidden="true">
        <rect x="1" y="1" width="58" height="38" fill="var(--trail-orange)"/>
        <polyline points="2,3 30,24 58,3" fill="none" stroke="var(--sky-blue)" stroke-width="3"/>
        <line x1="2" y1="38" x2="23" y2="19" stroke="var(--sky-blue)" stroke-width="3"/>
        <line x1="58" y1="38" x2="37" y2="19" stroke="var(--sky-blue)" stroke-width="3"/>
      </svg>
      <span>tallpinecolin@mailvane.net</span>
    </div>

    <div class="contact contact-phone">
      <svg class="contact-icon" width="60" height="44" viewBox="0 0 60 44" aria-hidden="true">
        <path d="M10 4 l8 -2 l6 11 l-5 4 c3 8 8 13 15 17 l4 -5 l11 6 l-2 7 c-2 2 -5 3 -8 2 c-16 -5 -27 -17 -31 -32 c-1 -4 0 -7 2 -8 z" fill="var(--trail-orange)"/>
      </svg>
      <span>+61472 836 915</span>
    </div>

    <div class="peak-artwork" role="img" aria-label="Mountain peaks with a climber raising both arms"></div>

    <p class="role">Adventure Guide</p>
  </div>
</body>
</html>
```